Cedar Row Maintenance and Concierge Flyer

We need a flyer for cedar row maintenance and concierge service. We specialize in and provide residential maintenance and errand services to retired and semi retired persons living in the Lake Norman area. The services we include:
Lighting and plumbing repairs
Ceiling fan installation
Handicap accessories
Locks and security
Picture hanging
Hang blinds
Furniture arrangement / assembly
Pressure washing
Battery Jump start
and more...

Our Concierge services include:
Errand running
Grocery shopping
Wellness Checks
Dog Walk
Garbage Collection
and more...

We offer monthly service agreements and 24/7 access
Call text or e-mail for more information
704.555.0187
1cedarrowmaint@quillpostmail.com

The design should invoke a sense of trust and a customer service driven mission

Target Market(s)

Residential maintenance

Industry/Entity Type

Property Maintenance

Contact Information for Business Card

Derek Halvorsen
48176 Quimby Ferrel Rd.
Cornelius NC 28031
704.555.0187
with uploaded logo

Requirements
Nice to have
• Would like a postcard size flyer. Front and back
Should not have
• No pics of of people wearing hard hats or pics of blueprints. No pics of commercial or industrial maintenance.

```html
<!DOCTYPE html>
<html lang="en">
<head>
<meta charset="utf-8">
<title>Cedar Row Maintenance and Concierge Flyer</title>
<link href="https://fonts.googleapis.com/css2?family=Montserrat:wght@300;400;500;600;800&family=Source+Sans+3:wght@400;500&display=swap" rel="stylesheet">
<style>
  :root {
    --ink: #1d1d1b;
    --accent-red: #d92b32;
    --brand-grey: #6d6e71;
    --paper: #ffffff;
  }
  * { margin: 0; padding: 0; box-sizing: border-box; }
  html, body { width: 1200px; height: 720px; overflow: hidden; background: var(--paper); }
  .flyer {
    position: relative;
    width: 1200px;
    height: 720px;
    background: var(--paper);
    color: var(--ink);
    font-family: "Montserrat", sans-serif;
    font-weight: 300;
  }
  .intro {
    position: absolute;
    top: 70px;
    left: 0;
    width: 1200px;
    text-align: center;
    font-size: 35px;
    line-height: 41px;
    letter-spacing: 0.3px;
  }
  .service-list {
    position: absolute;
    top: 218px;
    font-size: 27px;
    line-height: 37px;
    letter-spacing: 0.4px;
  }
  .service-list.maintenance { left: 63px; }
  .service-list.concierge { left: 578px; top: 221px; }
  .service-list h2 {
    color: var(--accent-red);
    font-weight: 600;
    font-size: 29px;
    line-height: 36px;
    margin-bottom: 3px;
  }
  .service-list h2 .colon { color: var(--ink); font-weight: 300; }
  .service-list ul { list-style: none; }
  .service-list li::before {
    content: "";
    display: inline-block;
    width: 6px;
    height: 6px;
    border-radius: 50%;
    background: var(--accent-red);
    vertical-align: middle;
    margin: -4px 10px 0 2px;
  }
  .brand-name {
    position: absolute;
    top: 478px;
    left: 104px;
    width: 370px;
    display: flex;
    align-items: center;
    gap: 14px;
    font-size: 21px;
    line-height: 27px;
    font-weight: 500;
    color: var(--brand-grey);
    letter-spacing: 0.5px;
  }
  .brand-name .mark {
    width: 60px;
    height: 60px;
    flex: none;
  }
  .agreements {
    position: absolute;
    top: 588px;
    left: 100px;
    width: 360px;
    text-align: center;
    font-family: "Source Sans 3", sans-serif;
    font-weight: 400;
    font-size: 22px;
    line-height: 31px;
  }
  .contact {
    position: absolute;
    top: 490px;
    left: 560px;
    width: 570px;
    text-align: center;
  }
  .contact .prompt {
    font-family: "Source Sans 3", sans-serif;
    font-weight: 400;
    font-size: 32px;
    letter-spacing: -0.3px;
    line-height: 40px;
  }
  .contact .phone {
    display: block;
    margin-top: 14px;
    color: var(--accent-red);
    font-weight: 800;
    font-size: 61px;
    line-height: 64px;
    letter-spacing: 1px;
  }
  .contact .email {
    display: block;
    margin-top: 2px;
    font-family: "Source Sans 3", sans-serif;
    font-weight: 400;
    font-size: 30px;
    line-height: 38px;
  }
</style>
</head>
<body>
<main class="flyer">
  <p class="intro">We specialize in and provide residential maintenance<br>and errand&nbsp; services to retired and semi retired persons<br>living in the Lake Norman area.</p>

  <section class="service-list maintenance">
    <h2>The services we include:</h2>
    <ul>
      <li>Lighting and plumbing repairs</li>
      <li>Ceiling fan installation</li>
      <li>Handicap accessories</li>
      <li>Locks and security</li>
    </ul>
    <p>and more...</p>
  </section>

  <section class="service-list concierge">
    <h2>Our Concierge services include<span class="colon">:</span></h2>
    <ul>
      <li>Errand running</li>
      <li>Grocery shopping</li>
      <li>Wellness Checks</li>
      <li>Garbage Collection</li>
    </ul>
    <p>and more...</p>
  </section>

  <div class="brand-name">
    <svg class="mark" viewBox="0 0 60 60" aria-hidden="true"><circle cx="30" cy="30" r="28" fill="var(--accent-red)"/></svg>
    <span>Cedar Row<br>Maintenance &amp; Concierge</span>
  </div>

  <p class="agreements">We offer monthly service<br>agreements and 24/7 access</p>

  <section class="contact">
    <p class="prompt">Call text or e-mail for more information</p>
    <a class="phone">704.555.0187</a>
    <a class="email">1cedarrowmaint@quillpostmail.com</a>
  </section>
</main>
</body>
</html>
```